Upgrades and adjustments to my existing website

I currently have a website in the trial period with HostBramble but their template isn't meeting my site needs. My website is https://www.QuorvaPosts.example. I need the calendar to be changed. Each customer that orders a real estate sign installation from us needs to be able to request a day (not time specific) and be able to enter the address of the home where they need the sign installed. In addition, I would like a testimonials section on the website. I need someone to build the website and point it to my domain name as I do not know how to do any of that. My customers are trying to order now so every day they can't place the order I am losing money so quick turn time is important

Target Market(s)

Real Estate Agents ordering sign post installations

Industry/Entity Type

Real Estate

Coding

Coded - Design and coding required

Number of Pages Required

1 page

Font styles to use
Sans Serif

Colors
0355a3
3377b5
85abd2
0493ce
33a6d7
85cae6

Requirements
Must have
• The ability to book installation requests online with address for installation. Please see live current website I have
Nice to have
• Links to social media, ability to pay invoice on website,
Testimonial section.
Ability to track progress of installation request for customers
Ability to share the appointment calendar with my installers

```html
<!DOCTYPE html>
<html lang="en">
<head>
<meta charset="utf-8">
<title>Quorva Posts</title>
<link rel="stylesheet" href="https://fonts.googleapis.com/css2?family=Montserrat:ital,wght@0,400;0,500;0,600;0,700;1,600;1,700&family=Poppins:wght@400;500&display=swap">
<style>
:root{
  --navy:#132f4a;
  --navy-deep:#0f2840;
  --royal:#0355a3;
  --sky:#0493ce;
  --sky-bright:#33a6d7;
  --pale:#f1f9fe;
  --white:#ffffff;
  --ink:#1d2b3a;
  --grey:#9a9a9a;
  --star:#f4c20d;
}
*{box-sizing:border-box;margin:0;padding:0}
html,body{width:1200px;height:2256px;overflow:hidden}
body{font-family:'Montserrat',sans-serif;background:var(--white);position:relative;color:var(--ink)}
.abs{position:absolute}
.center{text-align:center;left:0;width:1200px}

/* header + hero */
.top{top:0;left:0;width:1200px;height:533px;background:var(--navy)}
.brand{left:210px;top:38px;display:flex;align-items:center;gap:8px;color:var(--white);font-weight:700;font-size:20px;line-height:1.1}
.brand-mark{width:14px;height:14px;background:var(--sky-bright)}
.nav{top:74px;right:202px;display:flex;gap:22px;font-size:11px;color:var(--white)}
.nav .active{color:var(--sky-bright)}
.hero{left:200px;top:120px;width:800px;height:343px;background:var(--white);padding:6px}
.hero-inner{display:flex;height:100%}
.hero-photo{width:453px;height:100%;background:linear-gradient(160deg,#4fb8e0 0%,#5a7fa0 45%,#6b5a4a 100%)}
.hero-panel{flex:1;background:var(--royal);padding:83px 0 0 23px;color:var(--white)}
.hero-panel .welcome{font-weight:700;font-size:19px;letter-spacing:1px}
.hero-panel .big{font-weight:700;font-size:44px;color:var(--sky-bright);letter-spacing:1px;line-height:1.2;margin-left:-3px}
.hero-panel p{font-size:12px;line-height:14px;margin-top:16px;width:280px}
.btn-outline{display:inline-block;border:2px solid var(--sky-bright);color:var(--sky-bright);font-weight:700;font-size:15px;letter-spacing:1px;padding:8px 21px;margin-top:32px;margin-left:2px}

/* about */
.about{top:533px;left:0;width:1200px;height:300px;background:var(--pale)}
.sec-title{font-weight:700;font-size:24px;letter-spacing:.5px}
.rule{width:80px;height:3px;margin:4px auto 0}
.about .sec-title{color:var(--sky)}
.about .rule{background:var(--sky)}
.about h3{font-style:italic;font-weight:600;font-size:19px;color:var(--royal)}
.about p{left:292px;width:616px;text-align:center;font-size:12.3px;line-height:18.7px;color:var(--ink)}

/* services */
.services{top:833px;left:0;width:1200px;height:683px;background:var(--royal);color:var(--white)}
.services .rule{background:var(--white)}
.services .sub{font-style:italic;font-weight:700;font-size:15px}
.svc-frame{width:313px;height:281px;background:var(--white);padding:6px;box-shadow:0 2px 6px rgba(0,0,0,.3)}
.svc-photo{width:100%;height:100%}
.svc-name{font-weight:700;font-size:15.5px;width:313px;text-align:center;letter-spacing:.3px}
.svc-meta{font-size:15px;width:313px;text-align:center}
.btn-white{width:187px;height:43px;border:2px solid var(--white);font-weight:500;font-size:15px;letter-spacing:.5px;display:flex;align-items:center;justify-content:center}

/* testimonials */
.testimonials{top:1516px;left:0;width:1200px;height:435px;background:var(--white)}
.testimonials .sec-title{color:var(--navy)}
.testimonials .rule{background:var(--navy)}
.card{width:226px;font-family:'Poppins',sans-serif;text-align:center}
.card.featured{background:var(--white);box-shadow:0 0 10px rgba(0,0,0,.12);height:222px}
.avatar{width:50px;height:50px;border-radius:50%;background:#e3e6ea;margin:18px auto 0}
.card .name{font-weight:500;font-size:11px;color:#333;margin-top:12px}
.card .role{font-size:6.5px;letter-spacing:.5px;color:#888;margin-top:3px}
.card .quote{font-size:8.5px;line-height:16px;color:var(--grey);margin:10px auto 0;width:150px}
.stars{display:flex;gap:4px;justify-content:center;margin-top:8px}
.stars svg{width:8px;height:8px}
.dots{top:1909px;left:581px;display:flex;gap:3px}
.dots span{width:7px;height:7px;border-radius:50%;background:#999}
.dots span:first-child{background:var(--royal)}

/* footer */
.footer{top:1951px;left:0;width:1200px;height:242px;background:var(--navy);color:var(--white)}
.foot-brand{font-weight:500;font-size:15px}
.foot-head{font-weight:600;font-size:9px;letter-spacing:.3px}
.foot-text{font-size:9px;line-height:15px}
.socials{display:flex;gap:3px}
.socials span{width:22px;height:22px;border-radius:50%;background:var(--sky-bright)}
.subscribe{width:187px;height:35px;border:1px solid #7fa3c6;padding:3px;display:flex;align-items:center}
.subscribe .field{flex:1;font-size:8.5px;padding-left:5px}
.subscribe .send{width:40px;height:27px;background:var(--sky);display:flex;align-items:center;justify-content:center}
.bottom{top:2193px;left:0;width:1200px;height:63px;background:var(--navy-deep);color:var(--white);font-size:10px;display:flex;align-items:center;justify-content:center}
</style>
</head>
<body>

<section class="abs top">
  <div class="abs brand"><span class="brand-mark"></span><span>Quorva<br>Posts</span></div>
  <nav class="abs nav">
    <span>HOME</span><span>ABOUT US</span><span>SERVICES</span><span>TESTIMONIALS</span><span class="active">BOOK NOW</span><span>CONTACT US</span>
  </nav>
  <div class="abs hero">
    <div class="hero-inner">
      <div class="hero-photo" role="img" aria-label="Owner leaning on a real estate sign post with a for-sale panel in a park"></div>
      <div class="hero-panel">
        <div class="welcome">WELCOME TO</div>
        <div class="big">QUORVA POSTS</div>
        <p>We install solar powered lit real estate signs to make your home stand out and get it sold.</p>
        <div class="btn-outline">BOOK NOW</div>
      </div>
    </div>
  </div>
</section>

<section class="abs about">
  <div class="abs center" style="top:26px"><div class="sec-title">ABOUT US</div><div class="rule"></div></div>
  <h3 class="abs center" style="top:102px">Don’t sell your home in the dark</h3>
  <p class="abs" style="top:149px">We install solar powered lit real estate signs to make your home stand out and get it sold. We use treated wood posts with powder-coated steel bases for high quality, looks and durability. Your order includes storage, maintenance, and installation of your panels and riders within 48 hours, as well as free pick-up and removal. We are fully insured. Our Owner and Operator, Marlon, is committed to providing an excellent product and exceptional service.</p>
</section>

<section class="abs services">
  <div class="abs center" style="top:40px"><div class="sec-title">OUR SERVICES</div><div class="rule"></div></div>
  <div class="abs center sub" style="top:95px">Select any time and we will install within 48 hours</div>
  <div class="abs svc-frame" style="left:260px;top:172px"><div class="svc-photo" role="img" aria-label="White sign posts stored in a shed" style="background:linear-gradient(90deg,#8c9297,#e8e8e6 45%,#c9b89a 80%,#6d6f72)"></div></div>
  <div class="abs svc-frame" style="left:621px;top:172px"><div class="svc-photo" role="img" aria-label="Owner standing beside a pickup truck loaded with sign posts" style="background:linear-gradient(160deg,#9fb3c3,#7a6c5c 50%,#2a2f38)"></div></div>
  <div class="abs svc-name" style="left:260px;top:488px">Real Estate Sign Installation</div>
  <div class="abs svc-meta" style="left:260px;top:517px">1 hr|Price varies</div>
  <div class="abs svc-name" style="left:621px;top:488px">Sign Removal</div>
  <div class="abs svc-meta" style="left:621px;top:517px">1 hr|Price varies</div>
  <div class="abs btn-white" style="left:323px;top:577px">SCEDULE NOW</div>
  <div class="abs btn-white" style="left:684px;top:577px">SCEDULE NOW</div>
</section>

<section class="abs testimonials">
  <div class="abs center" style="top:36px"><div class="sec-title">TESTIMONIALS</div><div class="rule"></div></div>

  <div class="abs card" style="left:251px;top:135px">
    <div class="avatar" role="img" aria-label="Customer portrait"></div>
    <div class="name">Talia Verne</div><div class="role">JAVASCRIPT</div>
    <div class="quote">This should be used to tell a story and let your users know about your product or service.</div>
    <div class="stars"><svg viewBox="0 0 10 10"><path fill="var(--star)" d="M5 0l1.5 3.3 3.5.3-2.7 2.3.8 3.5L5 7.6 1.9 9.4l.8-3.5L0 3.6l3.5-.3z"/></svg><svg viewBox="0 0 10 10"><path fill="var(--star)" d="M5 0l1.5 3.3 3.5.3-2.7 2.3.8 3.5L5 7.6 1.9 9.4l.8-3.5L0 3.6l3.5-.3z"/></svg><svg viewBox="0 0 10 10"><path fill="var(--star)" d="M5 0l1.5 3.3 3.5.3-2.7 2.3.8 3.5L5 7.6 1.9 9.4l.8-3.5L0 3.6l3.5-.3z"/></svg><svg viewBox="0 0 10 10"><path fill="#999" d="M5 0l1.5 3.3 3.5.3-2.7 2.3.8 3.5L5 7.6 1.9 9.4l.8-3.5L0 3.6l3.5-.3z"/></svg><svg viewBox="0 0 10 10"><path fill="#999" d="M5 0l1.5 3.3 3.5.3-2.7 2.3.8 3.5L5 7.6 1.9 9.4l.8-3.5L0 3.6l3.5-.3z"/></svg></div>
  </div>

  <div class="abs card featured" style="left:487px;top:135px">
    <div class="avatar" role="img" aria-label="Customer portrait"></div>
    <div class="name">Oren Castel</div><div class="role">WEB DESIGNER</div>
    <div class="quote">This should be used to tell a story and let your users know about your product or service.</div>
    <div class="stars"><svg viewBox="0 0 10 10"><path fill="var(--star)" d="M5 0l1.5 3.3 3.5.3-2.7 2.3.8 3.5L5 7.6 1.9 9.4l.8-3.5L0 3.6l3.5-.3z"/></svg><svg viewBox="0 0 10 10"><path fill="var(--star)" d="M5 0l1.5 3.3 3.5.3-2.7 2.3.8 3.5L5 7.6 1.9 9.4l.8-3.5L0 3.6l3.5-.3z"/></svg><svg viewBox="0 0 10 10"><path fill="var(--star)" d="M5 0l1.5 3.3 3.5.3-2.7 2.3.8 3.5L5 7.6 1.9 9.4l.8-3.5L0 3.6l3.5-.3z"/></svg><svg viewBox="0 0 10 10"><path fill="var(--star)" d="M5 0l1.5 3.3 3.5.3-2.7 2.3.8 3.5L5 7.6 1.9 9.4l.8-3.5L0 3.6l3.5-.3z"/></svg><svg viewBox="0 0 10 10"><path fill="#999" d="M5 0l1.5 3.3 3.5.3-2.7 2.3.8 3.5L5 7.6 1.9 9.4l.8-3.5L0 3.6l3.5-.3z"/></svg></div>
  </div>

  <div class="abs card" style="left:723px;top:135px">
    <div class="avatar" role="img" aria-label="Customer portrait"></div>
    <div class="name">Deven Holt</div><div class="role">WEB DEVELOPER</div>
    <div class="quote">This should be used to tell a story and let your users know about your product or service.</div>
    <div class="stars"><svg viewBox="0 0 10 10"><path fill="var(--star)" d="M5 0l1.5 3.3 3.5.3-2.7 2.3.8 3.5L5 7.6 1.9 9.4l.8-3.5L0 3.6l3.5-.3z"/></svg><svg viewBox="0 0 10 10"><path fill="var(--star)" d="M5 0l1.5 3.3 3.5.3-2.7 2.3.8 3.5L5 7.6 1.9 9.4l.8-3.5L0 3.6l3.5-.3z"/></svg><svg viewBox="0 0 10 10"><path fill="var(--star)" d="M5 0l1.5 3.3 3.5.3-2.7 2.3.8 3.5L5 7.6 1.9 9.4l.8-3.5L0 3.6l3.5-.3z"/></svg><svg viewBox="0 0 10 10"><path fill="var(--star)" d="M5 0l1.5 3.3 3.5.3-2.7 2.3.8 3.5L5 7.6 1.9 9.4l.8-3.5L0 3.6l3.5-.3z"/></svg><svg viewBox="0 0 10 10"><path fill="var(--star)" d="M5 0l1.5 3.3 3.5.3-2.7 2.3.8 3.5L5 7.6 1.9 9.4l.8-3.5L0 3.6l3.5-.3z"/></svg></div>
  </div>
</section>
<div class="abs dots"><span></span><span></span><span></span><span></span></div>

<footer class="abs footer">
  <div class="abs foot-brand" style="left:217px;top:36px">Quorva Posts</div>
  <div class="abs foot-text" style="left:217px;top:84px;width:215px">We install solar powered lit real estate signs to make your home stand out and get it sold. We use treated wood posts with powder-coated steel bases for high quality, looks and durability.</div>
  <div class="abs socials" style="left:219px;top:176px" aria-label="Social links"><span></span><span></span><span></span><span></span><span></span></div>

  <div class="abs foot-head" style="left:467px;top:54px">CONTACT INFO</div>
  <div class="abs foot-text" style="left:467px;top:84px">555-014-2368<br>Orders@QuorvaPosts.example<br>www.quorvaposts.example</div>

  <div class="abs foot-head" style="left:617px;top:54px">OFFICE HOURS</div>
  <div class="abs foot-text" style="left:617px;top:84px;line-height:19px;margin-top:-2px">Mon- Fri - 9:00 am - 5:00pm<br>Saturday- 9:00 am - 2:00 pm<br>Sunday- Closed</div>

  <div class="abs foot-head" style="left:810px;top:54px">SUBSCRIBE NEWSLETTERS</div>
  <div class="abs foot-text" style="left:810px;top:84px;width:190px">Stay always in touch, subscribe to our newsleters</div>
  <div class="abs subscribe" style="left:810px;top:118px">
    <span class="field">your email id</span>
    <span class="send"><svg width="11" height="11" viewBox="0 0 12 12"><path fill="#fff" d="M12 0L0 5l5 1.5L6.5 12z"/></svg></span>
  </div>
  <div class="abs foot-text" style="left:810px;top:168px">Don't worry, we don't span</div>
</footer>
<div class="abs bottom">© 2021, Quorva Posts, all Rights reserved</div>

</body>
</html>
```